Business Cards for a law firm

Business cards for our law firm. Use our silhoette logo and OAK HARBOR - check our website (www.oakharbor-legal.com)

Contact Information for Business Card

our silhouette logo, OAK HARBOR, 800-555-0147, Dorian Kestrup, dorian@oakharbor-legal.com

Requirements
Must have
• our silhouette logo, OAK HARBOR, 800-555-0147, Dorian Kestrup, dorian@oakharbor-legal.com

```html
<!DOCTYPE html>
<html lang="en">
<head>
<meta charset="utf-8">
<title>Oak Harbor – Business Cards</title>
<link rel="stylesheet" href="https://fonts.googleapis.com/css2?family=Jost:wght@300;500;600&display=swap">
<style>
  :root {
    --navy: #1b3169;
    --orange: #f2a51f;
    --white: #ffffff;
    --page: #ffffff;
    --mark: #ffffff;
    --seal: #c9ced6;
  }
  * { margin: 0; padding: 0; box-sizing: border-box; }
  html, body { width: 1200px; height: 1015px; overflow: hidden; background: var(--page); }
  .canvas { position: relative; width: 1200px; height: 1015px; }

  .card {
    position: absolute;
    left: 299px;
    width: 630px;
    height: 360px;
    background: var(--navy);
    overflow: hidden;
    box-shadow: 0 14px 40px rgba(0,0,0,0.18);
  }
  .card--front { top: 104px; }
  .card--back { top: 536px; }

  /* Front */
  .brand {
    position: absolute;
    left: 0; right: 0;
    top: 142px;
    display: flex;
    justify-content: center;
    align-items: center;
    gap: 18px;
  }
  .brand__mark {
    width: 58px;
    height: 58px;
    background: var(--mark);
  }
  .brand__name {
    font-family: "Jost", sans-serif;
    font-weight: 500;
    font-size: 38px;
    letter-spacing: 0.1em;
    color: var(--white);
    line-height: 1;
  }
  .website {
    position: absolute;
    left: 0; right: 0;
    top: 294px;
    text-align: center;
    font-family: "Jost", sans-serif;
    font-weight: 600;
    font-size: 14px;
    letter-spacing: 0.42em;
    color: var(--orange);
    text-transform: uppercase;
  }

  /* Back */
  .portrait-area {
    position: absolute;
    left: 0; top: 0;
    width: 262px; height: 360px;
    background: var(--white);
  }
  .guarantee-seal {
    position: absolute;
    left: 99px; top: 104px;
    width: 164px; height: 184px;
    border-radius: 14px;
    background: var(--seal);
  }
  .contact {
    position: absolute;
    right: 29px;
    top: 50px;
    text-align: right;
    font-family: "Jost", sans-serif;
    color: var(--white);
  }
  .contact__name {
    font-weight: 500;
    font-size: 26px;
    letter-spacing: 0.28em;
    margin-right: -0.28em;
    line-height: 30px;
  }
  .contact__title {
    font-weight: 500;
    font-size: 17px;
    letter-spacing: 0.24em;
    margin-right: -0.24em;
    color: var(--orange);
    line-height: 22px;
  }
  .contact__pitch {
    margin-top: 32px;
    font-weight: 500;
    font-size: 13px;
    letter-spacing: 0.08em;
    line-height: 16px;
    text-transform: uppercase;
  }
  .contact__phone {
    margin-top: 12px;
    display: flex;
    justify-content: flex-end;
    align-items: center;
    gap: 10px;
    font-weight: 600;
    font-size: 27px;
    letter-spacing: 0.16em;
    margin-right: -0.16em;
    color: var(--orange);
    line-height: 34px;
  }
  .contact__email {
    margin-top: 28px;
    display: flex;
    justify-content: flex-end;
    align-items: center;
    gap: 12px;
    font-weight: 300;
    font-size: 24px;
    line-height: 30px;
  }
  .icon { flex: none; }
</style>
</head>
<body>
<div class="canvas">

  <section class="card card--front">
    <div class="brand">
      <div class="brand__mark" aria-hidden="true"></div>
      <div class="brand__name">OAK HARBOR</div>
    </div>
    <div class="website">www.oakharbor-legal.com</div>
  </section>

  <section class="card card--back">
    <div class="portrait-area" role="img" aria-label="White silhouette of an attorney in a suit, shown from the shoulders"></div>
    <div class="guarantee-seal" role="img" aria-label="Guarantee seal"></div>

    <div class="contact">
      <div class="contact__name">DORIAN KESTRUP</div>
      <div class="contact__title">INJURY ATTORNEY</div>
      <div class="contact__pitch">
        Injured?<br>Call<br>Oak Harbor!<br>Contact us for a free
      </div>
      <div class="contact__phone">
        <svg class="icon" width="26" height="26" viewBox="0 0 24 24" fill="none" stroke="var(--white)" stroke-width="1.3" aria-hidden="true">
          <path d="M5 3 L9 3 L10.5 7.5 L8.5 9 C9.7 11.6 12.4 14.3 15 15.5 L16.5 13.5 L21 15 L21 19 C21 20 20 21 19 21 C10.5 20.5 3.5 13.5 3 5 C3 4 4 3 5 3 Z"/>
        </svg>
        <span>(800) 555 0147</span>
      </div>
      <div class="contact__email">
        <svg class="icon" width="22" height="16" viewBox="0 0 22 16" fill="none" stroke="var(--white)" stroke-width="1.3" aria-hidden="true">
          <rect x="1" y="1" width="20" height="14"/>
          <path d="M1 1 L11 9 L21 1 M1 15 L8 7 M21 15 L14 7"/>
        </svg>
        <span>dorian@oakharbor-legal.com</span>
      </div>
    </div>
  </section>

</div>
</body>
</html>
```